Chinese Herbal and Roots Shop design

Hello Designers,

We are a herbal startup company which sells Chinese Herbal Products. we are looking for a responsive and unqiue Ecommerce web design.
Our business name is velorin and our area of business cut across the entire United States.

We don't have a logo at the moment and designers who come up with a great logo is more likely to be awarded winner of the consent.

The design needs to be completely custom design and we are not after just a template design. Please be creative and at the same time design have to be professionally looking and easy to navigate.
A theme which suits a herbal products are desired. We are open to different colors excpet RED and PINK.

NAVIGATION
Header -
Home, products, offers, Blog, cart, login/account

Footer -
Please refer to other Ecommerce websites

Page requires:
HOME PAGE
1. slider(Highlist products)
2. FEATURE PRODUCTS
3. Latest products
4. Most selling products
5. Deal of the day
6. Email capture (Newsletter/signup)
7. Social media links
8. Footer

PRODUCT PAGE
All the products will be present here with required details (price, short note and offers if any)

PRODUCT DETAILS PAGE
A well designed detailed page for a particular product covers the details of the price, increment, short description, purchase and other add to cart button. A section with similar products should be listed below aswell.

Industry/Entity Type

It Company

Coding

Coded - Design and coding required

```html
<!DOCTYPE html>
<html lang="en">
<head>
<meta charset="utf-8">
<title>Velorin – Chinese Herbal Products</title>
<link href="https://fonts.googleapis.com/css2?family=Montserrat:wght@400;500;600;700&family=Open+Sans:wght@400;600&display=swap" rel="stylesheet">
<style>
:root{
  --green:#6aa516;
  --green-dark:#5a9210;
  --ink:#222;
  --muted:#777;
  --line:#e2e2e2;
  --band:#ececec;
  --hero-a:#eef0f3;
  --hero-b:#dfe3e8;
  --white:#fff;
  --strike:#888;
}
*{box-sizing:border-box;margin:0;padding:0}
html,body{width:1200px;height:3429px;overflow:hidden}
body{position:relative;background:var(--white);font-family:"Open Sans",Arial,sans-serif;color:var(--ink)}
.abs{position:absolute}
.heading{font-family:"Montserrat",Arial,sans-serif;font-weight:700;color:var(--green);text-transform:uppercase}
.btn{position:absolute;display:flex;align-items:center;justify-content:center;font-family:"Montserrat",Arial,sans-serif;font-weight:600;text-transform:uppercase}
.btn-solid{background:var(--green);color:var(--white)}
.btn-outline{border:1px solid var(--green);color:var(--green);background:var(--white)}
.btn-more{border:1px solid #d66;color:#d44;font-size:10px;font-weight:500;background:var(--white)}
.photo{position:absolute}

/* header */
.site-header{position:absolute;left:0;top:0;width:1200px;height:91px;background:var(--white)}
.brand{position:absolute;left:130px;top:22px;font-family:"Montserrat",Arial,sans-serif;font-weight:400;font-size:38px;color:var(--green)}
.nav a{position:absolute;top:36px;height:28px;line-height:28px;font-family:"Montserrat",Arial,sans-serif;font-size:11px;font-weight:600;color:var(--ink);text-decoration:none;text-transform:uppercase}
.nav a.active{background:var(--green);color:var(--white);padding:0 10px}
.cart-box{position:absolute;left:872px;top:32px;width:196px;height:36px;border:1px solid var(--green);display:flex}
.cart-box span{display:flex;align-items:center;justify-content:center;gap:6px;font-family:"Montserrat",Arial,sans-serif;font-size:10px;font-weight:700;text-transform:uppercase}
.cart-box .cart{width:100px;color:var(--ink)}
.cart-box .login{flex:1;background:var(--green);color:var(--white)}
.cart-count{position:absolute;left:862px;top:24px;width:20px;height:20px;border-radius:50%;border:1px solid var(--green);background:var(--white);font-size:10px;color:var(--ink);text-align:center;line-height:18px}

/* hero */
.hero{position:absolute;left:0;top:91px;width:1200px;height:538px;background:linear-gradient(90deg,var(--hero-a),var(--hero-b))}
.hero h1{position:absolute;left:135px;top:64px;font-size:42px;line-height:1;letter-spacing:.5px}
.hero h2{position:absolute;left:135px;top:118px;font-family:"Montserrat",Arial,sans-serif;font-weight:500;font-size:38px;color:var(--green)}
.hero p{position:absolute;left:135px;top:184px;font-size:14px;color:#444}
.hero .shop{left:283px;top:357px;width:190px;height:59px;font-size:18px;clip-path:polygon(0 0,100% 0,92% 100%,0 100%)}
.dots{position:absolute;left:546px;top:488px;display:flex;gap:12px}
.dots i{width:10px;height:10px;border-radius:50%;background:#667;display:block}
.dots i.on{background:transparent;border:2px solid #667}

/* section headings */
.sec-title{position:absolute;left:130px;font-size:25px}
.sec-rule{position:absolute;left:130px;width:300px;height:2px;background:var(--green)}

/* featured */
.feat-item{position:absolute;width:200px;text-align:center}
.feat-item .name{font-family:"Montserrat",Arial,sans-serif;font-size:12px;font-weight:600;text-transform:uppercase}
.feat-item .price{margin-top:16px;font-family:"Montserrat",Arial,sans-serif;font-size:20px;font-weight:700;color:var(--green)}

/* latest */
.latest{position:absolute;left:0;top:1230px;width:1200px;height:548px;background:var(--band)}
.card{position:absolute;top:146px;width:224px;height:343px;background:var(--white);text-align:center}
.card .icons{position:absolute;left:12px;right:12px;top:10px;display:flex;justify-content:space-between}
.card .off{position:absolute;left:0;right:0;top:206px;font-size:10px;color:var(--muted)}
.card .name{position:absolute;left:0;right:0;top:222px;font-family:"Montserrat",Arial,sans-serif;font-size:12px;font-weight:600}
.card .prices{position:absolute;left:0;right:0;top:250px;font-family:"Montserrat",Arial,sans-serif;font-weight:700;font-size:20px;color:var(--green)}
.card .prices s{font-size:12px;font-weight:400;color:var(--strike);margin-right:4px}
.card .btn{left:65px;top:288px;width:94px;height:32px;font-size:12px}

/* deal */
.deal{position:absolute;left:610px;top:1778px;width:590px;height:508px;background:var(--green)}
.deal h3{position:absolute;left:53px;top:48px;font-family:"Montserrat",Arial,sans-serif;font-size:25px;color:var(--white);font-weight:700}
.deal .rule{position:absolute;left:53px;top:92px;width:382px;height:2px;background:var(--white)}
.deal .all{left:327px;top:103px;width:105px;height:25px;background:var(--white);color:var(--green);font-size:9px}
.deal-card{position:absolute;left:55px;top:138px;width:380px;height:320px;background:var(--white)}
.deal-card .txt{position:absolute;left:206px;top:30px;width:165px;font-family:"Montserrat",Arial,sans-serif;font-size:11px;font-weight:600;line-height:1.6;text-transform:uppercase}
.deal-card .from{position:absolute;left:206px;top:108px;font-size:10px;text-transform:uppercase;color:#444}
.deal-card .price{position:absolute;left:206px;top:124px;font-family:"Montserrat",Arial,sans-serif;font-weight:700;font-size:24px;color:var(--green)}
.deal-card .btn{left:204px;top:169px;width:109px;height:39px;font-size:14px}
.timeleft{position:absolute;left:34px;top:240px;font-size:10px;text-transform:uppercase}
.digits{position:absolute;left:34px;top:256px;display:flex;gap:2px}
.digits b{width:19px;height:32px;background:#333;color:var(--white);font-family:"Montserrat",Arial,sans-serif;font-size:22px;font-weight:500;text-align:center;line-height:32px}
.digits b.gap{margin-right:4px}
.units{position:absolute;left:34px;top:294px;display:flex;font-size:7px;color:#555;text-transform:uppercase}
.units span{width:44px;text-align:center}
.arrows{position:absolute;left:326px;top:292px;display:flex;gap:4px}
.arrows i{width:18px;height:18px;border:1px solid #bbb;display:flex;align-items:center;justify-content:center}

/* best sellers */
.best-item{position:absolute;top:2645px;width:140px;text-align:center;font-family:"Montserrat",Arial,sans-serif}
.best-item .name{font-size:12px;font-weight:600;text-transform:uppercase}
.best-item .price{margin-top:10px;font-size:17px;font-weight:700;color:var(--green)}
.best-item .stars{margin-top:4px}
.best-item .btn{position:relative;margin:34px auto 0;width:74px;height:22px;font-size:10px}
.arrow-circle{position:absolute;top:2526px;width:46px;height:46px;border-radius:50%;border:1px solid #ccc;background:var(--white);display:flex;align-items:center;justify-content:center}

/* newsletter */
.newsletter{position:absolute;left:0;top:2862px;width:1200px;height:190px;background:var(--band)}
.mail-badge{position:absolute;left:126px;top:-34px;width:68px;height:68px;border-radius:50%;background:var(--white);display:flex;align-items:center;justify-content:center}
.newsletter h4{position:absolute;left:130px;top:84px;font-size:25px;line-height:1.25}
.signup-form{position:absolute;left:347px;top:82px;width:721px;height:51px;background:var(--white);display:flex;align-items:center}
.signup-form .field{width:296px;padding-left:20px;display:flex;align-items:center;gap:16px;font-size:11px;text-transform:uppercase;color:#333;border-right:1px solid var(--line);height:100%}
.signup-form .btn{left:593px;top:8px;width:123px;height:35px;font-size:16px;gap:8px}

/* footer */
.footer-brand{position:absolute;left:130px;top:3148px;font-family:"Montserrat",Arial,sans-serif;font-size:38px;color:var(--green)}
.fcol{position:absolute;top:3104px}
.fcol h5{font-family:"Montserrat",Arial,sans-serif;font-size:10px;font-weight:600;text-transform:uppercase;margin-bottom:12px}
.fcol a{display:block;font-size:11px;color:#444;line-height:24px;text-decoration:none}
.contact-row{position:absolute;left:896px;display:flex;align-items:center;gap:18px;font-size:11px;color:#444;line-height:1.6}
.contact-row .ic{width:34px;height:34px;border-radius:50%;border:1px solid #bbb;display:flex;align-items:center;justify-content:center}
.bottom-bar{position:absolute;left:0;top:3338px;width:1200px;height:91px;border-top:1px solid var(--line)}
.follow{position:absolute;left:130px;top:34px;font-size:10px;text-transform:uppercase;font-weight:600;display:flex;align-items:center;gap:14px}
.follow i{width:22px;height:22px;border-radius:50%;background:var(--green);display:block}
.copy{position:absolute;right:130px;top:38px;font-size:10px;color:#555}
</style>
</head>
<body>

<header class="site-header">
  <div class="brand">Velorin</div>
  <nav class="nav">
    <a class="active" href="#" style="left:485px">Home</a>
    <a href="#" style="left:580px">Products</a>
    <a href="#" style="left:696px">Offers</a>
    <a href="#" style="left:798px">Blog</a>
  </nav>
  <div class="cart-count">0</div>
  <div class="cart-box">
    <span class="cart"><svg width="13" height="12" viewBox="0 0 13 12"><path d="M0 1h2l2 7h7l2-5H3" fill="none" stroke="#222" stroke-width="1.3"/><circle cx="5" cy="10.5" r="1" fill="#222"/><circle cx="10" cy="10.5" r="1" fill="#222"/></svg>My Cart</span>
    <span class="login"><svg width="10" height="12" viewBox="0 0 10 12"><rect x="1" y="5" width="8" height="7" fill="#fff"/><path d="M3 5V3a2 2 0 0 1 4 0v2" fill="none" stroke="#fff" stroke-width="1.4"/></svg>Login</span>
  </div>
</header>

<section class="hero">
  <h1 class="heading">Chinese Herbal</h1>
  <h2>Products</h2>
  <p>Lorem Ipsum is simply dummy and typesetting ...</p>
  <div class="photo" role="img" aria-label="White supplement bottle with purple cap" style="left:137px;top:240px;width:160px;height:252px;border-radius:28px 28px 14px 14px;background:linear-gradient(180deg,#6b4fb0 0 22%,#f4f4f4 22% 100%)"></div>
  <div class="btn btn-solid shop">Shop Now&nbsp;&nbsp;›</div>
  <div class="photo" role="img" aria-label="Wooden mortar and pestle filled with sliced herbal roots" style="left:583px;top:12px;width:492px;height:514px;border-radius:46% 46% 40% 40%;background:radial-gradient(circle at 45% 55%,#a0622c 0 30%,#d89a52 32% 62%,#e9b571 64% 70%,transparent 71%)"></div>
  <div class="dots"><i></i><i class="on"></i><i></i><i></i><i></i></div>
</section>

<!-- Featured products -->
<h3 class="heading sec-title" style="top:690px">Featured Products</h3>
<div class="sec-rule" style="top:742px"></div>
<div class="btn btn-more" style="left:903px;top:702px;width:167px;height:36px">More Feature Products</div>

<div class="feat-item" style="left:99px;top:800px">
  <div class="photo" role="img" aria-label="White bottle with green label" style="position:relative;margin:0 auto;width:90px;height:190px;border-radius:14px;background:linear-gradient(180deg,#f2f2f2 0 40%,#8cc63f 40% 70%,#f2f2f2 70%)"></div>
</div>
<div class="feat-item" style="left:300px;top:800px">
  <div class="photo" role="img" aria-label="Dark red supplement bottle with white label" style="position:relative;margin:0 auto;width:88px;height:190px;border-radius:12px;background:linear-gradient(180deg,#f4f4f4 0 15%,#8b1a1a 15% 50%,#eee 50% 78%,#8b1a1a 78%)"></div>
</div>
<div class="feat-item" style="left:506px;top:800px">
  <div class="photo" role="img" aria-label="Amber bottle with herbal label" style="position:relative;margin:0 auto;width:84px;height:190px;border-radius:10px;background:linear-gradient(180deg,#3a2412 0 22%,#ece6d8 22% 75%,#4a2e15 75%)"></div>
</div>
<div class="feat-item" style="left:700px;top:800px">
  <div class="photo" role="img" aria-label="Brown glass bottle with white label" style="position:relative;margin:0 auto;width:96px;height:190px;border-radius:14px;background:linear-gradient(180deg,#f5f5f5 0 18%,#5a2a10 18% 40%,#fafafa 40% 78%,#5a2a10 78%)"></div>
</div>
<div class="feat-item" style="left:899px;top:800px">
  <div class="photo" role="img" aria-label="Amber bottle with white cap" style="position:relative;margin:0 auto;width:76px;height:190px;border-radius:10px;background:linear-gradient(180deg,#f2f2f2 0 20%,#8a4b12 20%)"></div>
</div>

<div class="feat-item" style="left:99px;top:1030px"><div class="name">Heading 1</div><div class="price">$25.70</div></div>
<div class="feat-item" style="left:300px;top:1030px"><div class="name">Heading 2</div><div class="price">$35.70</div></div>
<div class="feat-item" style="left:506px;top:1030px"><div class="name">Heading 3</div><div class="price">$42.70</div></div>
<div class="feat-item" style="left:700px;top:1030px"><div class="name">Heading 4</div><div class="price">$42.70</div></div>
<div class="feat-item" style="left:899px;top:1030px"><div class="name">Heading 5</div><div class="price">$42.70</div></div>

<div class="btn btn-outline" style="left:142px;top:1111px;width:114px;height:30px;font-size:10px;font-weight:500">🛒&nbsp;Add to Cart</div>
<div class="btn btn-outline" style="left:343px;top:1111px;width:114px;height:30px;font-size:10px;font-weight:500">🛒&nbsp;Add to Cart</div>
<div class="btn btn-outline" style="left:549px;top:1111px;width:114px;height:30px;font-size:10px;font-weight:500">🛒&nbsp;Add to Cart</div>
<div class="btn btn-outline" style="left:743px;top:1111px;width:114px;height:30px;font-size:10px;font-weight:500">🛒&nbsp;Add to Cart</div>
<div class="btn btn-outline" style="left:942px;top:1111px;width:114px;height:30px;font-size:10px;font-weight:500">🛒&nbsp;Add to Cart</div>

<!-- Latest products -->
<section class="latest">
  <h3 class="heading sec-title" style="top:48px">Latest Products</h3>
  <div class="sec-rule" style="top:96px"></div>
  <div class="btn btn-more" style="left:914px;top:80px;width:156px;height:36px">More Latest Products</div>

  <article class="card" style="left:130px">
    <div class="icons"><span>☆</span><span>♡</span></div>
    <div class="photo" role="img" aria-label="Clear jar with honey-coloured contents and black lid" style="left:62px;top:32px;width:100px;height:150px;border-radius:12px;background:linear-gradient(180deg,#222 0 18%,#f1c36a 18%)"></div>
    <div class="off">5% OFF</div><div class="name">HEADING 1</div>
    <div class="prices"><s>$36.70</s>$22.70</div>
    <div class="btn btn-solid">Buy Now</div>
  </article>
  <article class="card" style="left:370px">
    <div class="icons"><span>☆</span><span>♡</span></div>
    <div class="photo" role="img" aria-label="Purple supplement tub with white lid" style="left:56px;top:32px;width:112px;height:150px;border-radius:12px;background:linear-gradient(180deg,#e9e9e9 0 22%,#5a4aa6 22%)"></div>
    <div class="off">2% OFF</div><div class="name">HEADING 2</div>
    <div class="prices"><s>$38.70</s>$21.70</div>
    <div class="btn btn-solid">Buy Now</div>
  </article>
  <article class="card" style="left:610px">
    <div class="icons"><span>☆</span><span>♡</span></div>
    <div class="photo" role="img" aria-label="Glass jar of herbal paste with gold lid" style="left:60px;top:32px;width:104px;height:150px;border-radius:12px;background:linear-gradient(180deg,#c7a04a 0 15%,#c99c5c 15%)"></div>
    <div class="off">10% OFF</div><div class="name">HEADING 3</div>
    <div class="prices"><s>$40.70</s>$26.70</div>
    <div class="btn btn-solid">Buy Now</div>
  </article>
  <article class="card" style="left:848px">
    <div class="icons"><span>☆</span><span>♡</span></div>
    <div class="photo" role="img" aria-label="White pill bottle with blue label" style="left:68px;top:32px;width:90px;height:150px;border-radius:12px;background:linear-gradient(180deg,#f3f3f3 0 30%,#2b4f9e 30% 60%,#f3f3f3 60%)"></div>
    <div class="off">8% OFF</div><div class="name">HEADING 4</div>
    <div class="prices"><s>$45.70</s>$30.70</div>
    <div class="btn btn-solid">Buy Now</div>
  </article>
</section>

<!-- Deal of the day -->
<div class="photo" role="img" aria-label="Wooden bowls of assorted dried Chinese herbs on a table" style="left:0;top:1778px;width:610px;height:508px;background:linear-gradient(135deg,#a07a5a,#6b3b2a 45%,#b08a68)"></div>
<section class="deal">
  <h3>DEAL OF THE DAY</h3>
  <div class="rule"></div>
  <div class="btn all">View All Deals</div>
  <div class="deal-card">
    <div class="photo" role="img" aria-label="Red jar with white label" style="left:28px;top:22px;width:141px;height:195px;border-radius:14px;background:linear-gradient(180deg,#555 0 12%,#b51c2c 12% 42%,#f4f4f4 42% 70%,#b51c2c 70%)"></div>
    <div class="txt">There are many variatio of passages of lorem psum available</div>
    <div class="from">Starting from</div>
    <div class="price">$21.70</div>
    <div class="btn btn-solid">Buy Now</div>
    <div class="timeleft">Time left</div>
    <div class="digits"><b>0</b><b class="gap">1</b><b>0</b><b class="gap">3</b><b>2</b><b class="gap">2</b><b>5</b><b>6</b></div>
    <div class="units"><span>Days</span><span>Hours</span><span>Min</span><span>Sec</span></div>
    <div class="arrows">
      <i><svg width="6" height="8" viewBox="0 0 6 8"><path d="M5 0L1 4l4 4" fill="none" stroke="#555"/></svg></i>
      <i><svg width="6" height="8" viewBox="0 0 6 8"><path d="M1 0l4 4-4 4" fill="none" stroke="#555"/></svg></i>
    </div>
  </div>
</section>

<!-- Most selling -->
<h3 class="heading" style="position:absolute;left:0;width:1200px;top:2350px;text-align:center;font-size:25px">Most Selling Products</h3>
<div style="position:absolute;left:450px;top:2404px;width:300px;height:2px;background:var(--green)"></div>

<div class="arrow-circle" style="left:144px"><svg width="8" height="12" viewBox="0 0 8 12"><path d="M7 1L2 6l5 5" fill="none" stroke="#555" stroke-width="1.5"/></svg></div>
<div class="arrow-circle" style="left:999px"><svg width="8" height="12" viewBox="0 0 8 12"><path d="M1 1l5 5-5 5" fill="none" stroke="#555" stroke-width="1.5"/></svg></div>

<div class="photo" role="img" aria-label="Black supplement bottle with red label" style="left:216px;top:2469px;width:72px;height:137px;border-radius:10px;background:linear-gradient(180deg,#111 0 40%,#c62828 40% 55%,#111 55%)"></div>
<div class="photo" role="img" aria-label="Small orange bottle with blue label" style="left:373px;top:2469px;width:40px;height:137px;border-radius:6px;background:linear-gradient(180deg,#eee 0 15%,#d4781c 15% 45%,#2c4c9a 45% 85%,#d4781c 85%)"></div>
<div class="photo" role="img" aria-label="White box beside an amber bottle" style="left:510px;top:2469px;width:122px;height:137px;background:linear-gradient(90deg,#f0f0f0 0 55%,transparent 55% 62%,#8c3a12 62%)"></div>
<div class="photo" role="img" aria-label="Plain white bottle" style="left:737px;top:2469px;width:72px;height:137px;border-radius:10px;background:linear-gradient(180deg,#e4e4e4 0 18%,#f7f7f7 18%)"></div>
<div class="photo" role="img" aria-label="Amber bottle with white label" style="left:912px;top:2469px;width:58px;height:137px;border-radius:8px;background:linear-gradient(180deg,#eee 0 20%,#a8561a 20% 45%,#f4f4f4 45% 75%,#a8561a 75%)"></div>

<div style="position:absolute;left:130px;top:2740px;width:940px;height:40px;box-shadow:0 18px 24px -14px rgba(0,0,0,.18)"></div>

<div class="best-item" style="left:181px"><div class="name">Heading 1</div><div class="price">$21.70</div><div class="stars" style="color:#c9a400;font-size:11px">★★★<span style="color:#bbb">☆☆</span></div><div class="btn btn-solid">Buy Now</div></div>
<div class="best-item" style="left:323px"><div class="name">Heading 2</div><div class="price">$18.99</div><div class="stars" style="color:#c9a400;font-size:11px">★★★<span style="color:#bbb">☆☆</span></div><div class="btn btn-solid">Buy Now</div></div>
<div class="best-item" style="left:501px"><div class="name">Heading 3</div><div class="price">$28.90</div><div class="stars" style="color:#c9a400;font-size:11px">★★★<span style="color:#bbb">☆☆</span></div><div class="btn btn-solid">Buy Now</div></div>
<div class="best-item" style="left:703px"><div class="name">Heading 4</div><div class="price">$32.50</div><div class="stars" style="color:#c9a400;font-size:11px">★★★<span style="color:#bbb">☆☆</span></div><div class="btn btn-solid">Buy Now</div></div>
<div class="best-item" style="left:870px"><div class="name">Heading 5</div><div class="price">$29.70</div><div class="stars" style="color:#c9a400;font-size:11px">★★★<span style="color:#bbb">☆☆</span></div><div class="btn btn-solid">Buy Now</div></div>

<!-- Newsletter -->
<section class="newsletter">
  <div class="mail-badge"><svg width="26" height="20" viewBox="0 0 26 20"><rect x="1" y="1" width="24" height="18" rx="2" fill="none" stroke="#6aa516" stroke-width="2"/><path d="M1 2l12 9 12-9" fill="none" stroke="#6aa516" stroke-width="2"/></svg></div>
  <h4 class="heading">Newsletter<br>Signup!</h4>
  <form class="signup-form">
    <div class="field"><svg width="10" height="11" viewBox="0 0 10 11"><circle cx="5" cy="3" r="2.6" fill="#333"/><path d="M0 11a5 5 0 0 1 10 0z" fill="#333"/></svg>Name</div>
    <div class="field" style="border:0"><svg width="12" height="9" viewBox="0 0 12 9"><rect width="12" height="9" fill="#333"/><path d="M0 0l6 5 6-5" fill="none" stroke="#fff"/></svg>E mail ID</div>
    <div class="btn btn-solid">Signup! <svg width="18" height="10" viewBox="0 0 18 10"><path d="M0 5h16M12 1l4 4-4 4" fill="none" stroke="#fff" stroke-width="2"/></svg></div>
  </form>
</section>

<!-- Footer -->
<footer>
  <div class="footer-brand">Velorin</div>
  <div class="fcol" style="left:398px"><h5>Information</h5><a href="#">Home</a><a href="#">Products</a><a href="#">Offrs</a><a href="#">Blog</a><a href="#">My Cart</a></div>
  <div class="fcol" style="left:553px"><h5>Customer Service</h5><a href="#">Contact Us</a><a href="#">Returns</a><a href="#">Site Map</a></div>
  <div class="fcol" style="left:736px"><h5>My Account</h5><a href="#">Account Login</a><a href="#">Order History</a><a href="#">Wish List</a><a href="#">Newsletter</a></div>
  <div class="fcol" style="left:896px"><h5>Contact Us</h5></div>
  <div class="contact-row" style="top:3149px"><span class="ic"><svg width="12" height="16" viewBox="0 0 12 16"><path d="M6 15S1 9 1 6a5 5 0 0 1 10 0c0 3-5 9-5 9z" fill="none" stroke="#6aa516" stroke-width="1.5"/><circle cx="6" cy="6" r="1.8" fill="#6aa516"/></svg></span><span>14 Linden Street<br>Ashford, AF2 7QL</span></div>
  <div class="contact-row" style="top:3199px"><span class="ic"><svg width="14" height="14" viewBox="0 0 14 14"><path d="M3 1l2 3-1.5 1.5a8 8 0 0 0 5 5L10 9l3 2-1.5 2.5C6 13 1 8 .5 2.5z" fill="none" stroke="#6aa516" stroke-width="1.3"/></svg></span><span>888.888.8888</span></div>
  <div class="contact-row" style="top:3250px"><span class="ic"><svg width="14" height="10" viewBox="0 0 14 10"><rect x=".5" y=".5" width="13" height="9" fill="none" stroke="#6aa516"/><path d="M.5 .5l6.5 5 6.5-5" fill="none" stroke="#6aa516"/></svg></span><span>info@velorin.com</span></div>

  <div class="bottom-bar">
    <div class="follow">Follow us :<span style="display:flex;gap:8px"><i aria-label="Social link"></i><i aria-label="Social link"></i><i aria-label="Social link"></i><i aria-label="Social link"></i></span></div>
    <div class="copy">Copyrights© 2017 All Rights Reserved</div>
  </div>
</footer>

</body>
</html>
```